Software Development Consulting Company Needs Business Card Design

We need a new business card design for our consultants at Verdant Systems (verdantsystems.example). We are a small firm that provides high-end software development and methodology consulting to medium to large enterprise IT organizations.

Our logo uses Futura for the font and we would like to stick with navy blue and canary yellow for the logo colors. Attached are normal and reversed versions of our logos in illustrator format.
Updates

Hi Everyone, Thank yo very much for your amazing design ideas. I have created a poll for this project and our employees will be voting on the design they wish to use. We will be making a decision this Wednesday (October 22nd). Thanks again, Marcus Hallward

Industry/Entity Type

Business

```html
<!DOCTYPE html>
<html lang="en">
<head>
<meta charset="utf-8">
<title>Verdant Systems – Business Card</title>
<link href="https://fonts.googleapis.com/css2?family=Open+Sans:wght@400;600&display=swap" rel="stylesheet">
<style>
  :root {
    --navy: #23486b;
    --canary: #f5dc1e;
    --paper: #ffffff;
    --backdrop: #ececed;
    --ink-soft: #3a4f66;
  }
  html, body {
    margin: 0;
    padding: 0;
    width: 1200px;
    height: 720px;
    overflow: hidden;
    background: var(--backdrop);
    font-family: "Open Sans", Arial, sans-serif;
  }
  .canvas {
    position: relative;
    width: 1200px;
    height: 720px;
  }
  .card {
    position: absolute;
    top: 212px;
    width: 520px;
    height: 297px;
    box-shadow: 0 2px 6px rgba(0, 0, 0, 0.12);
    overflow: hidden;
  }
  .card--front {
    left: 60px;
    background: var(--navy);
    display: flex;
    align-items: center;
    justify-content: center;
  }
  .card--back {
    left: 620px;
    background: var(--paper);
  }
  .wordmark {
    display: flex;
    align-items: center;
    gap: 14px;
  }
  .wordmark__dot {
    width: 10px;
    height: 10px;
    border-radius: 50%;
    background: var(--canary);
  }
  .wordmark__name {
    color: var(--paper);
    font-weight: 400;
    font-size: 26px;
    letter-spacing: 0.28em;
    text-transform: uppercase;
  }
  .back-panel {
    position: absolute;
    left: 0;
    top: 0;
    width: 172px;
    height: 100%;
    background: var(--navy);
  }
  .contact {
    position: absolute;
    right: 34px;
    top: 40px;
    text-align: right;
  }
  .contact__name {
    margin: 0;
    color: var(--navy);
    font-size: 22px;
    font-weight: 400;
    line-height: 1.1;
  }
  .contact__title {
    margin: 4px 0 0;
    color: var(--canary);
    font-size: 11px;
    letter-spacing: 0.3em;
  }
  .contact__details {
    list-style: none;
    margin: 62px 0 0;
    padding: 0;
    color: var(--ink-soft);
    font-size: 11px;
    line-height: 1.75;
  }
  .contact__details li {
    display: flex;
    align-items: center;
    justify-content: flex-end;
    gap: 6px;
  }
  .contact__icon {
    width: 11px;
    height: 11px;
  }
  .contact__details .no-icon {
    padding-right: 17px;
  }
</style>
</head>
<body>
<main class="canvas">
  <section class="card card--front" aria-label="Card front">
    <div class="wordmark">
      <span class="wordmark__dot"></span>
      <span class="wordmark__name">Verdant Systems</span>
    </div>
  </section>

  <section class="card card--back" aria-label="Card back">
    <div class="back-panel"></div>
    <div class="contact">
      <h1 class="contact__name">Daniel Porter</h1>
      <p class="contact__title">Sale Manager</p>
      <ul class="contact__details">
        <li>314-555-0187
          <svg class="contact__icon" viewBox="0 0 12 12" aria-hidden="true">
            <rect x="3" y="0.8" width="6" height="10.4" rx="1.2" fill="none" stroke="var(--canary)" stroke-width="1.2"/>
            <line x1="5" y1="9.4" x2="7" y2="9.4" stroke="var(--canary)" stroke-width="1"/>
          </svg>
        </li>
        <li>daniel.porter@verdantsystems.example
          <svg class="contact__icon" viewBox="0 0 12 12" aria-hidden="true">
            <rect x="0.8" y="2.5" width="10.4" height="7" fill="none" stroke="var(--canary)" stroke-width="1.1"/>
            <polyline points="0.8,2.5 6,6.6 11.2,2.5" fill="none" stroke="var(--canary)" stroke-width="1.1"/>
          </svg>
        </li>
        <li class="no-icon">4410 Maple Ridge Ct/ Fairview/ MO 63000</li>
      </ul>
    </div>
  </section>
</main>
</body>
</html>
```